Summer Sale Graphics for Social Media

I want to create 11 social media graphics (new Instagram size 4:5 (1080 x 1350 pixels) focusing on our Summer Sale Graphics, using any of the pics attached. Use the attached pics, NO RANDOM STOCK PHOTOGRAPHY. For the color scheme of the graphics, they should all be complementary to the product colors in the photos.
You can add any of the photos attached but none are required. You can do some of the graphics in all text. I mainly need BOLD text that says one of the headlines (11 total) SEE ATTACHED WORD DOCUMENT for the headlines to use.

```html
<!DOCTYPE html>
<html lang="en">
<head>
<meta charset="utf-8">
<title>Summer Sale Social Graphics</title>
<link href="https://fonts.googleapis.com/css2?family=Antonio:wght@300;500;600;700&family=Montserrat:wght@500;700;800&display=swap" rel="stylesheet">
<style>
:root{
  --page:#ebebeb;
  --plum:#a4497f;
  --plum-light:#c97aa9;
  --plum-dark:#7a2a5e;
  --wine:#8c1c5a;
  --blush:#f6c6de;
  --white:#ffffff;
  --ink:#3a2230;
  --gold:#ffe94a;
  --orange:#e0622a;
  --frame:#a08268;
}
*{margin:0;padding:0;box-sizing:border-box}
html,body{width:1200px;height:4167px;overflow:hidden;background:var(--page)}
.canvas{position:relative;width:1200px;height:4167px}
.tile{position:absolute;width:493px;height:616px;overflow:hidden;color:var(--white);
  background:radial-gradient(circle at 50% 40%,var(--plum-light) 0%,var(--plum) 55%,var(--plum-dark) 130%)}
.c1{left:78px}.c2{left:621px}.c3{left:353px}
.r1{top:66px}.r2{top:736px}.r3{top:1409px}.r4{top:2083px}.r5{top:2757px}.r6{top:3425px}
.abs{position:absolute;white-space:nowrap}
.center{left:0;right:0;text-align:center}
.cond{font-family:'Antonio',sans-serif;font-weight:700;letter-spacing:-.5px;line-height:1}
.thin{font-family:'Antonio',sans-serif;font-weight:300;line-height:1}
.sans{font-family:'Montserrat',sans-serif;font-weight:700}
.photo{position:absolute;background:linear-gradient(160deg,#d9c3b4 0%,#9a7a6a 45%,#4a3a38 100%)}
.bottles{position:absolute;border-radius:24px;background:linear-gradient(180deg,#ffffff 0%,#eeeeee 70%,#d8d8d8 100%)}
.sale-now{position:absolute;font-family:'Montserrat',sans-serif;font-weight:700;font-size:25px;letter-spacing:.5px;white-space:nowrap}
.offer{position:absolute;font-family:'Montserrat',sans-serif;font-weight:500;font-size:22px;white-space:nowrap}
.offer b{font-weight:800;font-size:31px}
.pill{position:absolute;left:50%;transform:translateX(-50%);width:260px;height:42px;display:flex;align-items:center;justify-content:center;
  background:linear-gradient(90deg,transparent,rgba(255,255,255,.3) 25%,rgba(255,255,255,.3) 75%,transparent);
  font-family:'Montserrat',sans-serif;font-weight:500;font-size:22px;gap:8px;white-space:nowrap}
.pill b{font-weight:800;font-size:31px}
.diag-light{position:absolute;background:rgba(255,255,255,.14)}
</style>
</head>
<body>
<main class="canvas">

  <section class="tile c1 r1">
    <div class="diag-light" style="inset:0;clip-path:polygon(200px 0,260px 0,190px 616px,130px 616px)"></div>
    <div class="photo" role="img" aria-label="Smiling woman in a brown sweater holding supplement bottles" style="inset:0;clip-path:polygon(250px 0,493px 0,493px 616px,185px 616px)"></div>
    <h2 class="abs cond" style="left:20px;top:86px;font-size:72px;line-height:78px">Your<br>Summer<br>Body<br>Won’t<br>Wait</h2>
    <div class="sale-now" style="left:22px;top:553px">SALE NOW!</div>
    <div class="offer" style="left:252px;top:548px">Up to <b>$15 OFF</b></div>
  </section>

  <section class="tile c2 r1">
    <div class="abs" style="left:146px;top:110px;width:200px;height:200px;border-radius:50%;background:rgba(255,255,255,.85)"></div>
    <div class="bottles" role="img" aria-label="Four supplement bottles lined up" style="left:74px;top:160px;width:345px;height:150px"></div>
    <h2 class="abs center cond" style="top:366px;font-size:58px;line-height:66px">Final Countdown<br>to Summer</h2>
    <div class="sale-now center" style="top:516px">SALE NOW!</div>
    <div class="pill" style="top:558px">Up to <b>$15 OFF</b></div>
  </section>

  <section class="tile c1 r2">
    <svg class="abs" style="left:0;top:0" width="493" height="616" aria-hidden="true">
      <path d="M24 385 V40 H469 V385 M24 385 h18 M451 385 h18" fill="none" stroke="rgba(255,255,255,.7)" stroke-width="2"/>
    </svg>
    <h2 class="abs center cond" style="top:76px;font-size:118px;line-height:138px">Detox,<br>Burn Fat,</h2>
    <p class="abs center thin" style="top:362px;font-size:42px">and Turn Heads This Summer</p>
    <div class="abs sans" style="left:139px;top:429px;width:215px;height:81px;background:var(--plum-dark);display:flex;align-items:center;justify-content:center;font-size:29px">SALE NOW!</div>
    <div class="offer center" style="top:544px">Up to <b>$15 OFF</b></div>
  </section>

  <section class="tile c2 r2">
    <div class="photo" role="img" aria-label="Smiling woman in a white top standing behind a row of supplement bottles" style="left:76px;top:65px;width:340px;height:340px;border-radius:50%"></div>
    <h2 class="abs center cond" style="top:414px;font-size:34px;line-height:47px;font-weight:600">Summer’s Here. And We’re Having<br>the <span style="color:var(--gold);font-weight:700;font-size:42px">Biggest Sale</span> of the Year</h2>
    <div class="diag-light" style="left:265px;top:546px;width:228px;height:60px;clip-path:polygon(20px 0,100% 0,100% 100%,0 100%)"></div>
    <div class="sale-now" style="left:70px;top:562px">SALE NOW!</div>
    <div class="offer" style="left:288px;top:558px">Up to <b>$15 OFF</b></div>
  </section>

  <section class="tile c1 r3">
    <div class="diag-light" style="inset:0;clip-path:polygon(200px 0,250px 0,200px 616px,150px 616px)"></div>
    <div class="photo" role="img" aria-label="Smiling woman in a white crop top holding a supplement bottle at a counter" style="inset:0;clip-path:polygon(250px 0,493px 0,493px 616px,180px 616px)"></div>
    <h2 class="abs cond" style="left:18px;top:164px;font-size:64px;line-height:72px">One Sale.<br>One Body.</h2>
    <p class="abs thin" style="left:24px;top:325px;font-size:54px;line-height:60px">One<br>Summer<br>to Slay</p>
    <div class="offer" style="left:243px;top:540px;color:var(--ink)">Up to <b>$15 OFF</b></div>
  </section>

  <section class="tile c2 r3">
    <div class="abs" style="inset:0;background:linear-gradient(180deg,#fbeff5 0%,#f0d2e1 45%,transparent 60%)"></div>
    <div class="diag-light" style="left:0;top:250px;width:493px;height:140px;background:var(--plum-light);clip-path:polygon(0 40%,100% 0,100% 100%,0 100%)"></div>
    <div class="bottles" role="img" aria-label="Four supplement bottles of different heights" style="left:34px;top:112px;width:420px;height:234px"></div>
    <h2 class="abs center cond" style="top:370px;font-size:56px">Summer Isn’t Waiting</h2>
    <p class="abs center thin" style="top:446px;font-size:44px">Neither Should You</p>
    <div class="sale-now center" style="top:530px">SALE NOW!</div>
    <div class="pill" style="top:573px">Up to <b>$15 OFF</b></div>
  </section>

  <section class="tile c1 r4">
    <div class="diag-light" style="inset:0;clip-path:polygon(190px 0,250px 0,180px 616px,120px 616px)"></div>
    <div class="photo" role="img" aria-label="Smiling woman in a brown sweater holding supplement bottles" style="inset:0;clip-path:polygon(245px 0,493px 0,493px 616px,190px 616px)"></div>
    <h2 class="abs cond" style="left:24px;top:116px;font-size:48px;line-height:54px;font-weight:600">Slim Waist.<br>Flat Tummy.<br>More Energy.</h2>
    <h2 class="abs cond" style="left:24px;top:282px;font-size:82px">Let’s Go!</h2>
    <div class="sale-now" style="left:22px;top:553px">SALE NOW!</div>
    <div class="offer" style="left:265px;top:548px">Up to <b>$15 OFF</b></div>
  </section>

  <section class="tile c2 r4">
    <div class="abs" style="left:46px;top:96px;width:400px;height:400px;border-radius:50%;border:2px solid rgba(255,255,255,.1)"></div>
    <svg class="abs" style="left:200px;top:20px" width="150" height="70" aria-hidden="true">
      <path d="M20 30 L70 12 L74 56 L28 46 Z" fill="var(--wine)"/>
      <path d="M102 20 L118 4 M108 34 L136 24 M98 8 L104 0" stroke="var(--wine)" stroke-width="5" stroke-linecap="round"/>
    </svg>
    <div class="abs cond" style="left:139px;top:76px;width:186px;height:82px;background:var(--blush);color:var(--wine);transform:rotate(-8deg);display:flex;align-items:center;justify-content:center;font-size:60px">Hurry!</div>
    <h2 class="abs center cond" style="top:200px;font-size:68px">Our Summer</h2>
    <p class="abs center thin" style="top:280px;font-size:66px">Slim-Down</p>
    <h2 class="abs center cond" style="top:356px;font-size:68px">Sale Is On</h2>
    <div class="abs center sans" style="top:474px;font-size:46px">Don’t Miss It!</div>
    <div class="pill" style="top:573px">Up to <b>$15 OFF</b></div>
  </section>

  <section class="tile c1 r5" style="background:var(--frame)">
    <div class="photo" role="img" aria-label="Smiling woman in a white top behind a row of supplement bottles in a kitchen" style="inset:13px 13px 0 13px"></div>
    <div class="abs" style="left:13px;right:13px;bottom:0;height:240px;background:linear-gradient(180deg,transparent,rgba(255,255,255,.92) 45%,#ffffff)"></div>
    <div class="abs cond" style="left:38px;top:28px;font-size:100px;line-height:112px;text-align:center;width:60px">S<br>A<br>L<br>E</div>
    <p class="abs thin" style="left:104px;top:446px;font-size:44px;color:var(--ink);font-weight:500">Your Summer Body</p>
    <h2 class="abs center cond" style="top:502px;font-size:50px;color:var(--ink)">Starts Here</h2>
    <div class="offer center" style="top:558px;color:var(--orange)">Up to <b>$15 OFF</b></div>
  </section>

  <section class="tile c2 r5">
    <div class="abs" style="left:28px;top:80px;width:437px;height:230px;background:var(--plum-dark);transform:rotate(-3deg);opacity:.6"></div>
    <div class="abs" style="left:23px;top:73px;width:443px;height:235px;background:var(--wine);transform:rotate(-3deg)"></div>
    <h2 class="abs center cond" style="top:126px;font-size:70px;line-height:82px">Limited-Time<br>Summer Sale</h2>
    <svg class="abs" style="left:0;top:0" width="493" height="616" aria-hidden="true">
      <path d="M130 408 H26 V616 M363 408 H467 V616" fill="none" stroke="rgba(255,255,255,.75)" stroke-width="2"/>
    </svg>
    <p class="abs center thin" style="top:382px;font-size:54px">Snatch Your</p>
    <h2 class="abs center cond" style="top:446px;font-size:56px">Supplements Now!</h2>
    <div class="pill" style="top:576px">Up to <b>$15 OFF</b></div>
  </section>

  <section class="tile c3 r6">
    <div class="abs" style="left:96px;top:230px;width:300px;height:200px;border-radius:50%;background:rgba(255,255,255,.1)"></div>
    <h2 class="abs center cond" style="top:46px;font-size:64px;line-height:82px">Get Snatched for<br>Summer</h2>
    <div class="bottles" role="img" aria-label="Four supplement bottles lined up" style="left:44px;top:240px;width:371px;height:177px"></div>
    <div class="abs center sans" style="top:452px;font-size:37px">Supplements On</div>
    <div class="abs center sans" style="top:504px;font-size:50px">Sale Now!</div>
    <div class="pill" style="top:571px">Up to <b>$15 OFF</b></div>
  </section>

</main>
</body>
</html>
```